" Nossa empresa, RCT (Rede Costa Tropical), opera no setor de telecomunicações, fornecendo serviços de internet de alta qualidade para os moradores da cidade de Taubaté "

```html
<!DOCTYPE html>
<html lang="pt-BR">
<head>
<meta charset="UTF-8">
<title>RCT – Cartão de visita</title>
<link href="https://fonts.googleapis.com/css2?family=Montserrat:wght@400;500;800&display=swap" rel="stylesheet">
<style>
  :root {
    --bg: #e9eaec;
    --navy: #1c2680;
    --ink: #1d2a5e;
    --white: #ffffff;
    --muted: #4a5070;
    --green: #3fbf5a;
    --orange: #f0782a;
    --blue: #2a8ed8;
  }
  * { margin: 0; padding: 0; box-sizing: border-box; }
  html, body { width: 1200px; height: 1200px; overflow: hidden; }
  body {
    background: var(--bg);
    font-family: "Montserrat", Arial, sans-serif;
    position: relative;
  }
  .card {
    position: absolute;
    left: 283px;
    width: 636px;
    height: 340px;
  }
  .card-front {
    top: 200px;
    background: var(--navy);
    color: var(--white);
  }
  .card-back {
    top: 643px;
    background: var(--white);
    color: var(--ink);
  }
  .front-brand {
    position: absolute;
    top: 90px;
    left: 0;
    width: 100%;
    text-align: center;
  }
  .brand-line {
    display: inline-flex;
    align-items: center;
    gap: 18px;
  }
  .brand-dot {
    width: 34px; height: 34px; border-radius: 50%;
    background: var(--white);
  }
  .brand-name {
    font-weight: 800;
    font-size: 96px;
    line-height: 1;
    letter-spacing: 2px;
  }
  .brand-sub {
    display: block;
    margin-top: 6px;
    font-weight: 800;
    font-size: 17px;
    letter-spacing: 3px;
    text-transform: uppercase;
  }
  .front-web {
    position: absolute;
    top: 285px;
    left: 0;
    width: 100%;
    display: flex;
    justify-content: center;
    align-items: center;
    gap: 10px;
    font-size: 22px;
  }
  .back-brand {
    position: absolute;
    top: 62px;
    left: 30px;
    color: var(--navy);
  }
  .back-brand .brand-line { gap: 10px; }
  .back-brand .brand-dot { width: 20px; height: 20px; background: var(--navy); }
  .back-brand .brand-name { font-size: 58px; }
  .back-brand .brand-sub { font-size: 10px; letter-spacing: 2px; margin-top: 3px; }
  .contacts {
    position: absolute;
    top: 68px;
    left: 345px;
    font-size: 25px;
    font-weight: 500;
  }
  .contact-row {
    display: flex;
    align-items: center;
    gap: 14px;
  }
  .contact-row + .contact-row { margin-top: 20px; }
  .icon-stack { display: flex; flex-direction: column; gap: 6px; }
  .icon-square {
    width: 24px; height: 24px; border-radius: 5px;
  }
  .icon-square.phone { background: var(--green); }
  .icon-square.social-a { background: var(--orange); }
  .icon-square.social-b { background: var(--blue); }
  .person {
    position: absolute;
    top: 222px;
    left: 30px;
  }
  .person-name { font-size: 25px; font-weight: 500; }
  .person-role { font-size: 15px; margin-top: 6px; color: var(--muted); }
</style>
</head>
<body>
  <section class="card card-front">
    <div class="front-brand">
      <div class="brand-line">
        <span class="brand-dot"></span>
        <span class="brand-name">RCT</span>
      </div>
      <span class="brand-sub">Rede Costa Tropical</span>
    </div>
    <div class="front-web">
      <svg width="22" height="22" viewBox="0 0 24 24" fill="none" stroke="#ffffff" stroke-width="2">
        <circle cx="12" cy="12" r="10"/>
        <ellipse cx="12" cy="12" rx="4.5" ry="10"/>
        <line x1="2" y1="12" x2="22" y2="12"/>
      </svg>
      <span>redecostatropical.com.br</span>
    </div>
  </section>

  <section class="card card-back">
    <div class="back-brand">
      <div class="brand-line">
        <span class="brand-dot"></span>
        <span class="brand-name">RCT</span>
      </div>
      <span class="brand-sub">Rede Costa Tropical</span>
    </div>
    <div class="contacts">
      <div class="contact-row">
        <span class="icon-square phone"></span>
        <span>00 98765 4321</span>
      </div>
      <div class="contact-row">
        <div class="icon-stack">
          <span class="icon-square social-a"></span>
          <span class="icon-square social-b"></span>
        </div>
        <span>/redecostatropical</span>
      </div>
    </div>
    <div class="person">
      <p class="person-name">Nome e Sobrenome</p>
      <p class="person-role">Cargo / Função</p>
    </div>
  </section>
</body>
</html>
```